Clear Plastic Card Design

I am looking to have a business card designed from my logo icon. I am looking to match the style of a different business card I have attached in the files.
Looking for a card that is plastic, with layers of transparency in the shape of my logo icon (also attached in the files) - not a circle like the other card. The winning design will incorporate the red icon logo on the front and back and include the charity's name, "Lanterns of Willow Creek" in the same or similar font, as well as an email and phone number. For now, use the email: email@lanternsofwillowcreek.org and the phone number 555-014-7392.
We like how the sample business card has transparency, partial and full opacity layers and a matching color scheme. Files will need to be in vector so that our business card printing company can work with it.
UPDATE:
We've some excellent designs in, thank you everyone! I got an early review from the owner, and he requested a minor redirect to find his perfect design. He wants the design to stand out by NOT being a rectangle. Try instead a circle, square, or best yet - something that falls in the outline of the logo icon, either fully or partially. Thank you, everyone!
Lanterns of Willow Creek text should be incorporated as well as a phone and email.

```html
<!DOCTYPE html>
<html lang="en">
<head>
<meta charset="utf-8">
<title>Lanterns of Willow Creek — Business Card</title>
<link rel="stylesheet" href="https://fonts.googleapis.com/css2?family=Questrial&display=swap">
<style>
  :root {
    --page-bg: #ffffff;
    --card-frost: #c6d0cf;
    --card-frost-light: #d4dcdb;
    --card-edge: #e3e9e8;
    --ink: #1e2222;
    --mark-red: #e5352b;
  }
  * { margin: 0; padding: 0; box-sizing: border-box; }
  html, body {
    width: 1200px;
    height: 846px;
    overflow: hidden;
    background: var(--page-bg);
  }
  body {
    font-family: "Questrial", "Century Gothic", sans-serif;
    color: var(--ink);
    position: relative;
  }
  .card {
    position: absolute;
    width: 540px;
    height: 340px;
    border-radius: 22px;
    background: linear-gradient(160deg, var(--card-frost-light), var(--card-frost));
    border: 3px solid var(--card-edge);
    box-shadow: 0 10px 26px rgba(40, 60, 60, 0.22);
  }
  .card--front { left: 40px; top: 253px; }
  .card--back { left: 620px; top: 253px; }

  .brand {
    position: absolute;
    display: flex;
    align-items: center;
    gap: 14px;
  }
  .brand__name {
    font-size: 26px;
    line-height: 1.05;
    color: var(--ink);
    text-align: right;
  }
  .brand__square {
    width: 72px;
    height: 72px;
    background: var(--mark-red);
    flex: none;
  }
  .card--front .brand { right: 44px; top: 74px; }
  .card--back .brand { right: 44px; top: 92px; }

  .contact {
    position: absolute;
    left: 40px;
    bottom: 58px;
    font-size: 22px;
    line-height: 1.3;
    color: var(--ink);
  }
</style>
</head>
<body>
  <section class="card card--front" aria-label="Card front">
    <div class="brand">
      <p class="brand__name">Lanterns of<br>Willow Creek</p>
      <span class="brand__square" aria-hidden="true"></span>
    </div>
    <div class="contact">
      <p class="contact__phone">Phone: 555-014-7392</p>
      <p class="contact__email">email@lanternsofwillowcreek.org</p>
    </div>
  </section>

  <section class="card card--back" aria-label="Card back">
    <div class="brand">
      <p class="brand__name">Lanterns of<br>Willow Creek</p>
      <span class="brand__square" aria-hidden="true"></span>
    </div>
  </section>
</body>
</html>
```